Stunning website design for world's unique software

Design only (No coding required)
This website design is linked with a logo design and illustration design contests.

Industry/Entity Type

Software

```html
<!DOCTYPE html>
<html lang="en">
<head>
<meta charset="utf-8">
<title>tandem – Unique HID Emulator</title>
<link rel="stylesheet" href="https://fonts.googleapis.com/css2?family=Ubuntu:wght@400;500&family=Caveat:wght@500&display=swap">
<style>
  :root {
    --header-grey: #efefef;
    --brand-orange: #ef7300;
    --ink: #2b2220;
    --nav-ink: #333333;
    --body-ink: #3a3a3a;
    --tile-grey: #ececec;
    --air-blue: #1f6fc0;
    --play-blue: #2aa1dd;
    --copy-green: #2f7a3d;
    --white: #ffffff;
  }
  * { box-sizing: border-box; margin: 0; padding: 0; }
  html, body { width: 1200px; height: 796px; overflow: hidden; background: var(--white); }
  body { position: relative; font-family: "Ubuntu", sans-serif; color: var(--body-ink); }

  .site-header { position: absolute; left: 0; top: 0; width: 1200px; height: 117px; background: var(--header-grey); }
  .brand { position: absolute; left: 68px; top: 30px; display: flex; align-items: center; gap: 14px; }
  .brand-mark { width: 56px; height: 56px; background: var(--brand-orange); }
  .brand-name { font-weight: 500; font-size: 56px; line-height: 1; color: var(--ink); letter-spacing: 0.5px; }

  .main-nav a { position: absolute; top: 56px; font-size: 17.5px; color: var(--nav-ink); text-decoration: none; }
  .free-hint { position: absolute; left: 623px; top: 18px; font-family: "Caveat", cursive; font-size: 19px; color: var(--brand-orange); }
  .free-arrow { position: absolute; left: 693px; top: 40px; }

  .tagline-band { position: absolute; left: 0; top: 121px; width: 1200px; height: 50px; background: var(--brand-orange);
    color: var(--white); font-size: 26px; line-height: 50px; text-align: center; padding-left: 6px; }

  .device-showcase { position: absolute; left: 286px; top: 239px; width: 612px; height: 251px;
    background: linear-gradient(90deg, #2c8fd6 0%, #7dbb1f 40%, #f2c21c 72%, #e8780f 100%); border-radius: 8px; }

  .intro { position: absolute; left: 0; top: 530px; width: 1206px; text-align: center; font-size: 15.5px; line-height: 26px; color: var(--body-ink); }

  .feature { position: absolute; top: 635px; width: 141px; height: 141px; text-align: center; }
  .feature.is-active { background: var(--tile-grey); border: 1px solid var(--brand-orange); }
  .feature svg { position: absolute; left: 50%; top: 53px; transform: translate(-50%, -50%); }
  .feature-label { position: absolute; left: 0; right: 0; top: 108px; font-size: 15.5px; color: var(--nav-ink); }
</style>
</head>
<body>
  <header class="site-header">
    <div class="brand">
      <span class="brand-mark"></span>
      <span class="brand-name">tandem</span>
    </div>
    <nav class="main-nav">
      <a href="#" style="left:563px">tandem?</a>
      <a href="#" style="left:655px">Download</a>
      <a href="#" style="left:772px">Buy now</a>
      <a href="#" style="left:876px">Manual</a>
      <a href="#" style="left:956px">Forum</a>
    </nav>
    <span class="free-hint">Try tandem for free</span>
    <svg class="free-arrow" width="14" height="16" viewBox="0 0 14 16" aria-hidden="true">
      <path d="M7 1 V13 M2 8 L7 14 L12 8" fill="none" stroke="var(--brand-orange)" stroke-width="1.6"/>
    </svg>
  </header>

  <div class="tagline-band">World’s Airwave Unique HID Emulator</div>

  <div class="device-showcase" role="img" aria-label="Laptop, monitor, tablet and phone showing video screens"></div>

  <p class="intro">Tandem makes Airwave controller equipped PC or Orchard work as standard Airwave keyboard/mouse combo.<br>
  So, you can seamlessly controll your smart devices inclusing computer, smartphone and tablet PC with the computer’s keyboard and mouse</p>

  <div class="feature is-active" style="left:334px">
    <svg width="66" height="74" viewBox="0 0 66 74" aria-hidden="true">
      <ellipse cx="33" cy="37" rx="31" ry="35" fill="var(--air-blue)"/>
    </svg>
    <span class="feature-label">Airwave</span>
  </div>

  <div class="feature" style="left:533px">
    <svg width="74" height="74" viewBox="0 0 74 74" aria-hidden="true">
      <circle cx="37" cy="37" r="35" fill="var(--play-blue)"/>
      <path d="M28 21 L54 37 L28 53 Z" fill="var(--white)"/>
    </svg>
    <span class="feature-label">Controller</span>
  </div>

  <div class="feature" style="left:728px">
    <svg width="92" height="92" viewBox="0 0 92 92" aria-hidden="true">
      <circle cx="46" cy="46" r="45" fill="var(--copy-green)"/>
      <g fill="none" stroke="var(--white)" stroke-width="2">
        <rect x="27" y="24" width="22" height="30" rx="2"/>
        <rect x="42" y="38" width="22" height="30" rx="2" fill="var(--copy-green)"/>
        <path d="M32 31h12M32 37h8M32 43h6M47 45h12M47 51h12M47 57h12M47 63h8"/>
      </g>
    </svg>
    <span class="feature-label">Copy</span>
  </div>
</body>
</html>
```